International Food Company needs packaging design for new products

We have a logo for our new business. It is attached. Now we need a packaging design for the products that we will be selling. We are an international wholesale foods company selling foods and herbs that will be certified organic and Non-GMO imported from West Africa. We are just in the process of launching new products. We're looking for a design that is fresh and modern.

Here is a list of items that we are requesting packaging design for.

Baobob Powder-8 oz and 12 oz
Dried Mango- 8 oz
Mango Powder 8 oz and 12 oz

```html
<!DOCTYPE html>
<html lang="en">
<head>
<meta charset="utf-8">
<title>Sunvale Farms – Dried Mango Packaging</title>
<link rel="stylesheet" href="https://fonts.googleapis.com/css2?family=Oswald:wght@300;500;600&family=Montserrat:wght@400;600&display=swap">
<style>
  :root {
    --bg: #fbf0ef;
    --pouch-white: #ffffff;
    --pouch-shade: #eeeeee;
    --seal-line: #dcdcdc;
    --leaf-green: #3b6121;
    --brand-green: #6fae3c;
    --orange: #ee8a3b;
    --orange-light: #f6b57a;
    --yellow: #f2c443;
    --yellow-light: #f8dc82;
    --mango-deep: #e0902c;
    --mango-light: #f6c868;
    --size-dot: #2b2b2b;
    --badge-line: #7b8c6a;
  }
  * { box-sizing: border-box; margin: 0; padding: 0; }
  html, body { width: 1200px; height: 849px; overflow: hidden; }
  body {
    background: var(--bg);
    font-family: "Montserrat", sans-serif;
    position: relative;
  }
  .pouch {
    position: absolute;
    top: 140px;
    width: 320px;
    height: 576px;
    border-radius: 14px 14px 8px 8px;
    overflow: hidden;
    background: linear-gradient(90deg, var(--pouch-shade) 0%, var(--pouch-white) 12%, var(--pouch-white) 88%, var(--pouch-shade) 100%);
  }
  .pouch--orange { left: 222px; --band: var(--orange); --band-light: var(--orange-light); }
  .pouch--yellow { left: 678px; --band: var(--yellow); --band-light: var(--yellow-light); }

  .pouch__seal {
    position: absolute; left: 0; right: 0; top: 26px;
    height: 1px; background: var(--seal-line);
  }
  .pouch__seal--lower { top: 34px; }

  .brand {
    position: absolute; top: 62px; left: 0; right: 0;
    display: flex; flex-direction: column; align-items: center; gap: 10px;
  }
  .brand__dot {
    width: 30px; height: 30px; border-radius: 50%;
    background: var(--brand-green);
  }
  .brand__name {
    font-family: "Oswald", sans-serif; font-weight: 300;
    font-size: 20px; letter-spacing: 1.5px; color: var(--brand-green);
  }

  .product-title {
    position: absolute; top: 196px; left: 0; right: 0;
    text-align: center;
    font-family: "Oswald", sans-serif; font-weight: 600;
    font-size: 66px; line-height: 56px; letter-spacing: 1px;
    color: var(--leaf-green);
  }
  .product-title__rule {
    position: absolute; top: 326px; left: 112px;
    width: 96px; height: 2px; background: var(--leaf-green);
  }

  .color-band {
    position: absolute; left: 0; right: 0; top: 356px; bottom: 0;
    background: linear-gradient(180deg, var(--band-light) 0%, var(--band) 35%, var(--band) 100%);
  }

  .product-photo {
    position: absolute; top: 340px; left: 62px;
    width: 226px; height: 162px;
    border-radius: 48% 52% 40% 45% / 45% 50% 45% 50%;
    background: radial-gradient(circle at 40% 45%, var(--mango-light) 0%, var(--mango-deep) 70%, #c9741c 100%);
  }

  .net-weight {
    position: absolute; top: 490px; left: 22px;
    width: 30px; height: 30px; border-radius: 50%;
    background: var(--size-dot); color: #fff;
    font-size: 8px; font-weight: 600;
    display: flex; align-items: center; justify-content: center;
  }

  .badges {
    position: absolute; top: 484px; right: 22px;
    display: flex; gap: 14px;
  }
  .badge { display: flex; flex-direction: column; align-items: center; gap: 4px; }
  .badge__mark {
    width: 30px; height: 30px; border-radius: 50%;
    border: 1.5px solid var(--badge-line);
  }
  .badge__label {
    font-size: 5.5px; font-weight: 600; letter-spacing: .3px;
    color: var(--leaf-green); text-transform: uppercase;
  }
</style>
</head>
<body>

<section class="pouch pouch--orange">
  <div class="pouch__seal"></div>
  <div class="pouch__seal pouch__seal--lower"></div>
  <div class="brand">
    <span class="brand__dot"></span>
    <span class="brand__name">SUNVALE FARMS</span>
  </div>
  <h1 class="product-title">DRIED<br>MANGO</h1>
  <div class="product-title__rule"></div>
  <div class="color-band"></div>
  <div class="product-photo" role="img" aria-label="Photo of dried mango slices"></div>
  <div class="net-weight">8 oz</div>
  <div class="badges">
    <div class="badge"><span class="badge__mark"></span><span class="badge__label">Non-GMO</span></div>
    <div class="badge"><span class="badge__mark"></span><span class="badge__label">100% Organic</span></div>
  </div>
</section>

<section class="pouch pouch--yellow">
  <div class="pouch__seal"></div>
  <div class="pouch__seal pouch__seal--lower"></div>
  <div class="brand">
    <span class="brand__dot"></span>
    <span class="brand__name">SUNVALE FARMS</span>
  </div>
  <h1 class="product-title">DRIED<br>MANGO</h1>
  <div class="product-title__rule"></div>
  <div class="color-band"></div>
  <div class="product-photo" role="img" aria-label="Photo of dried mango slices"></div>
  <div class="net-weight">8 oz</div>
  <div class="badges">
    <div class="badge"><span class="badge__mark"></span><span class="badge__label">Non-GMO</span></div>
    <div class="badge"><span class="badge__mark"></span><span class="badge__label">100% Organic</span></div>
  </div>
</section>

</body>
</html>
```